Web app with questionnaires and graphs

For crewlifters.nl I want a clean design with good UX . It's a web app that let's users fill in questionnaires to assess things like team culture, psychological safety and so on. Colorwise should work with the Velmor Institute green logo. The app displays graphs (bar, line, pie) so these should also be incorporated.

```html
<!DOCTYPE html>
<html lang="en">
<head>
<meta charset="utf-8">
<title>Velmor Institute – Tools</title>
<link rel="stylesheet" href="https://fonts.googleapis.com/css2?family=Raleway:wght@400;500;600;700&display=swap">
<style>
  :root {
    --blue-deep: #1530a0;
    --blue-bright: #1d63dc;
    --page-grey: #e2e2e2;
    --card-white: #ffffff;
    --tool-card: #f3f3f3;
    --ink: #1b1b1b;
    --ink-soft: #555555;
    --ink-muted: #777777;
    --accent-green: #12a85a;
    --ring-yellow: #f6d13a;
    --ring-green: #4b9a1f;
    --nav-active: #2137a8;
    --nav-idle: #555555;
    --illus-light: #d7f1df;
    --illus-mid: #9fdcb1;
  }
  * { box-sizing: border-box; margin: 0; padding: 0; }
  html, body { width: 1200px; height: 2600px; overflow: hidden; }
  body {
    position: relative;
    background: var(--page-grey);
    font-family: "Raleway", sans-serif;
    color: var(--ink);
  }
  .hero-band {
    position: absolute; left: 0; top: 0; width: 1200px; height: 700px;
    background: linear-gradient(200deg, var(--blue-bright) 0%, #1a45c0 35%, var(--blue-deep) 100%);
  }
  .status-time {
    position: absolute; left: 74px; top: 42px;
    font-size: 46px; color: #fff; font-weight: 400; letter-spacing: 1px;
  }
  .status-icons { position: absolute; right: 74px; top: 54px; }
  .nav-back { position: absolute; left: 68px; top: 158px; }
  .brand-name {
    position: absolute; left: 0; width: 1200px; top: 162px; text-align: center;
    font-size: 50px; font-weight: 700; color: #fff; letter-spacing: 1px;
  }
  .nav-menu { position: absolute; right: 78px; top: 160px; }
  .hero-title {
    position: absolute; left: 0; width: 1200px; top: 308px; text-align: center;
    font-size: 46px; font-weight: 600; color: #fff;
  }
  .stat-card {
    position: absolute; top: 437px; width: 510px; height: 471px;
    background: var(--card-white); border-radius: 6px;
    box-shadow: 0 2px 6px rgba(0,0,0,0.15);
    text-align: center;
  }
  .stat-card.results { left: 71px; }
  .stat-card.count { left: 611px; }
  .stat-ring { position: absolute; left: 165px; top: 71px; }
  .stat-caption {
    position: absolute; left: 0; width: 100%; top: 326px;
    font-size: 22px; font-weight: 600; color: var(--ink-muted);
  }
  .stat-title {
    position: absolute; left: 0; width: 100%; top: 370px;
    font-size: 28px; font-weight: 600; color: var(--ink);
  }
  .intro-text {
    position: absolute; left: 95px; width: 1010px; top: 962px;
    text-align: center; font-size: 28px; line-height: 50px; color: var(--ink);
  }
  .tool-card {
    position: absolute; left: 73px; width: 1048px;
    background: var(--tool-card); border-radius: 4px;
    box-shadow: 0 2px 5px rgba(0,0,0,0.18);
  }
  .tool-card.safety { top: 1265px; height: 281px; }
  .tool-card.culture { top: 1593px; height: 320px; }
  .tool-card.developer { top: 1963px; height: 320px; }
  .tool-illustration {
    position: absolute; left: 32px; width: 222px; height: 200px;
    border-radius: 48% 52% 45% 55% / 55% 45% 55% 45%;
    background: radial-gradient(circle at 45% 45%, var(--illus-mid), var(--illus-light) 70%);
  }
  .safety .tool-illustration { top: 40px; }
  .culture .tool-illustration { top: 60px; height: 150px; }
  .developer .tool-illustration { top: 55px; }
  .tool-body { position: absolute; left: 307px; right: 60px; }
  .safety .tool-body { top: 48px; }
  .culture .tool-body { top: 48px; }
  .developer .tool-body { top: 50px; }
  .tool-name { font-size: 29px; font-weight: 600; color: var(--ink-soft); margin-bottom: 12px; }
  .tool-desc { font-size: 28px; line-height: 50px; color: var(--ink-soft); }
  .add-button {
    position: absolute; left: 1063px; width: 96px; height: 96px; border-radius: 50%;
    background: var(--accent-green);
    display: flex; align-items: center; justify-content: center;
  }
  .add-button.one { top: 1487px; }
  .add-button.two { top: 1863px; }
  .add-button.three { top: 2234px; }
  .bottom-nav {
    position: absolute; left: 0; top: 2361px; width: 1200px; height: 239px;
    background: #fff; border-top: 1px solid #d6d6d6;
  }
  .nav-item { position: absolute; top: 70px; }
</style>
</head>
<body>
  <div class="hero-band"></div>
  <div class="status-time">10.42</div>
  <svg class="status-icons" width="180" height="36" viewBox="0 0 180 36">
    <rect x="0" y="24" width="7" height="10" rx="1.5" fill="#fff"/>
    <rect x="11" y="18" width="7" height="16" rx="1.5" fill="#fff"/>
    <rect x="22" y="12" width="7" height="22" rx="1.5" fill="#fff"/>
    <rect x="33" y="4" width="7" height="30" rx="1.5" fill="#fff"/>
    <path d="M58 12 a30 30 0 0 1 40 0" stroke="#fff" stroke-width="5" fill="none" stroke-linecap="round"/>
    <path d="M65 20 a19 19 0 0 1 26 0" stroke="#fff" stroke-width="5" fill="none" stroke-linecap="round"/>
    <circle cx="78" cy="29" r="4" fill="#fff"/>
    <rect x="114" y="4" width="58" height="28" rx="7" fill="none" stroke="#fff" stroke-width="3"/>
    <rect x="119" y="9" width="48" height="18" rx="4" fill="#7ccb5a"/>
    <rect x="174" y="13" width="4" height="10" rx="1.5" fill="#fff"/>
  </svg>
  <svg class="nav-back" width="60" height="80" viewBox="0 0 60 80">
    <polyline points="50,4 8,40 50,76" fill="none" stroke="#fff" stroke-width="7"/>
  </svg>
  <div class="brand-name">Velmor Institute</div>
  <svg class="nav-menu" width="104" height="74" viewBox="0 0 104 74">
    <rect x="0" y="0" width="104" height="10" fill="#fff"/>
    <rect x="30" y="32" width="74" height="10" fill="#fff"/>
    <rect x="0" y="64" width="104" height="10" fill="#fff"/>
  </svg>
  <h1 class="hero-title">Free tools to strengthen your teams</h1>

  <section class="stat-card results">
    <svg class="stat-ring" width="180" height="180" viewBox="0 0 180 180">
      <circle cx="90" cy="90" r="82" fill="none" stroke="var(--ring-yellow)" stroke-width="14"
        stroke-dasharray="464 516" transform="rotate(-90 90 90)"/>
      <circle cx="90" cy="90" r="59" fill="#fff" stroke="#cccccc" stroke-width="1.5"/>
      <text x="86" y="101" text-anchor="middle" font-family="Raleway, sans-serif" font-weight="700" font-size="36" fill="#1b1b1b">90<tspan font-size="17" font-weight="500">%</tspan></text>
    </svg>
    <div class="stat-caption">Last Progress</div>
    <div class="stat-title">My Questionaire Results</div>
  </section>

  <section class="stat-card count">
    <svg class="stat-ring" width="180" height="180" viewBox="0 0 180 180">
      <path d="M90 8 A82 82 0 0 0 90 172" fill="none" stroke="var(--ring-green)" stroke-width="14"/>
      <circle cx="90" cy="90" r="59" fill="#fff" stroke="#cccccc" stroke-width="1.5"/>
      <text x="86" y="101" text-anchor="middle" font-family="Raleway, sans-serif" font-weight="700" font-size="36" fill="#1b1b1b">50<tspan font-size="17" font-weight="500">%</tspan></text>
    </svg>
    <div class="stat-caption">Completed Questionares</div>
    <div class="stat-title">Number Of Questionaires</div>
  </section>

  <p class="intro-text">To make your team - and organization - better, you first need to map out how things are now. Our tools give you insight into the health of your team and the culture of the organization. With the results in hand, you can start improving your team and your organization. Each tool gives you useful tips and tricks to make improvements. Are you stuck? We are happy to help you!</p>

  <article class="tool-card safety">
    <div class="tool-illustration" role="img" aria-label="Illustration of three colleagues collaborating around a green board"></div>
    <div class="tool-body">
      <h2 class="tool-name">Psychological safety</h2>
      <p class="tool-desc">Measure the psychological safety in your team completely anonymously.</p>
    </div>
  </article>

  <article class="tool-card culture">
    <div class="tool-illustration" role="img" aria-label="Illustration of two colleagues talking in an office with a desk and chair"></div>
    <div class="tool-body">
      <h2 class="tool-name">Halvern Culture Scan</h2>
      <p class="tool-desc">With this tool you visualize the general culture of your organization. Is it mainly a Control, Competence, Collaboration or Cultivation culture?</p>
    </div>
  </article>

  <article class="tool-card developer">
    <div class="tool-illustration" role="img" aria-label="Illustration of a developer at a desk surrounded by code windows"></div>
    <div class="tool-body">
      <h2 class="tool-name">Developer Culture Test</h2>
      <p class="tool-desc">Meet de Development cultuur in je organisatie. Hebben jullie wat nodig is om talent aan te trekken en te behouden?</p>
    </div>
  </article>

  <div class="add-button one"><svg width="48" height="48" viewBox="0 0 48 48"><path d="M24 4v40M4 24h40" stroke="#fff" stroke-width="5"/></svg></div>
  <div class="add-button two"><svg width="48" height="48" viewBox="0 0 48 48"><path d="M24 4v40M4 24h40" stroke="#fff" stroke-width="5"/></svg></div>
  <div class="add-button three"><svg width="48" height="48" viewBox="0 0 48 48"><path d="M24 4v40M4 24h40" stroke="#fff" stroke-width="5"/></svg></div>

  <nav class="bottom-nav">
    <svg class="nav-item" style="left:116px" width="80" height="84" viewBox="0 0 80 84">
      <path d="M40 2 L78 38 L70 38 L70 80 L50 80 L50 56 L30 56 L30 80 L10 80 L10 38 L2 38 Z" fill="var(--nav-active)" stroke="var(--nav-active)" stroke-width="4" stroke-linejoin="round"/>
    </svg>
    <svg class="nav-item" style="left:393px" width="88" height="84" viewBox="0 0 88 84">
      <g fill="none" stroke="var(--nav-idle)" stroke-width="4">
        <rect x="2" y="40" width="12" height="42"/><rect x="20" y="2" width="12" height="80"/>
        <rect x="38" y="52" width="12" height="30"/><rect x="56" y="30" width="12" height="52"/>
        <rect x="74" y="14" width="12" height="68"/>
      </g>
      <rect x="20" y="2" width="12" height="30" fill="var(--nav-idle)"/>
      <rect x="38" y="52" width="12" height="12" fill="var(--nav-idle)"/>
      <rect x="74" y="14" width="12" height="22" fill="var(--nav-idle)"/>
    </svg>
    <svg class="nav-item" style="left:706px" width="86" height="86" viewBox="0 0 86 86">
      <circle cx="43" cy="43" r="43" fill="var(--nav-idle)"/>
      <circle cx="43" cy="24" r="6" fill="#fff"/>
      <rect x="38" y="36" width="10" height="32" fill="#fff"/>
    </svg>
    <svg class="nav-item" style="left:996px" width="84" height="84" viewBox="0 0 84 84">
      <circle cx="42" cy="26" r="24" fill="var(--nav-idle)"/>
      <path d="M2 80 Q4 52 42 52 Q80 52 82 80 Z" fill="var(--nav-idle)"/>
    </svg>
  </nav>
</body>
</html>
```